Holiday Let Property Management Service and Website. We manage properties for holiday letting

We want a stylish business card that reflects our brand.
*** UPDATE *** PLEASE USE THE RECTANGULAR ORANGE COLOUR SWIPE PROVIDED IN THE DROP BOX FOR THE BSINESS CARD COLOUR.***
Please view the site: www.lodgewell.com.au
Obviously, we want to use the same logo font from our site for the card design.
We want to have the name "Lodgewell" right across the front in white and an orange background colour that matches the orange on our website or a brighter fresher looking orange .
We'd like to have the details on the back similar to what I've shown below but obviously with some more aesthetic added and better positioning than I have provided.
Same colours as the front. white writing and orange background. Once we have the design we'd like the font to be raised and the finish to be a low sheen. Quality thickness and finishes.
---------------------------------------------------------------------------
(Rough idea of writing details on back of card but open to nicer repositioning)

LODGEWELL
Holiday Let Management & Consulting Specialists

Marta Van Kerr Owen Brisk
Principal Director
0492637058 0487350216

email: enquiries@lodgewell.com.au
www.lodgewell.com.au

--------------------------------------------------------------------------

Target Market(s)

Property owners who may want to convert to holiday letting and people seeking holiday accommodation.

Industry/Entity Type

Tourism

Contact Information for Business Card

(Front of card) To have "Lodgewell" to stretch across the card in white writing the same font as our website home page. (discreetly including the logo TM if possible)

------------------------------------------------------------------------------------------------
(Back of card)

LODGEWELL
Holiday Let Consultants & Management Specialists

Marta Van Kerr Owen Brisk
Principal Director
0492637058 0487350216

www.lodgewell.com.au

-----------------------------------------------------------------------------------------------

Font styles to use
Other font styles liked:
• something similar or complimentary to our logo font please

Requirements
Must have
• The same font for our logo name and close to the same colour orange as the orange footer on our website. (if you can make it pop more without going too far away from it that would be great.)
• Orange background front and back with white font.
• *** UPDATE *** PLEASE USE THE RECTANGULAR ORANGE COLOUR SWIPE PROVIDED IN THE DROP BOX FOR THE BSINESS CARD COLOUR.***
Nice to have
• Great symmetry and aesthetics
Should not have
• Any other writing except our brand name (Lodgewell) on the front of the card and a small, discreet trade mark (TM)

```html
<!DOCTYPE html>
<html lang="en">
<head>
<meta charset="utf-8">
<title>Lodgewell Business Card</title>
<link rel="stylesheet" href="https://fonts.googleapis.com/css2?family=Archivo:wght@400;500;700;800&display=swap">
<style>
  :root {
    --orange: #e9933c;
    --white: #ffffff;
    --ink: #231f20;
    --rule: #4a4a4a;
    --edge: #6b6b6b;
  }
  * { margin: 0; padding: 0; box-sizing: border-box; }
  html, body {
    width: 1200px; height: 1200px; overflow: hidden;
    background: var(--white);
    font-family: "Archivo", "Helvetica Neue", Arial, sans-serif;
  }
  .canvas { position: relative; width: 1200px; height: 1200px; }

  .card {
    position: absolute; left: 180px; width: 838px; height: 479px;
    border-radius: 40px;
  }

  /* Front */
  .card-front { top: 100px; background: var(--orange); color: var(--white); }
  .brand-name {
    position: absolute; left: 0; right: 0; top: 242px;
    text-align: center;
    font-size: 128px; font-weight: 800; letter-spacing: -5px; line-height: 1;
  }
  .brand-name .tm {
    font-size: 12px; font-weight: 500; letter-spacing: 0;
    vertical-align: top; position: relative; top: 4px; margin-left: 4px;
  }
  .tagline {
    position: absolute; left: 0; right: 0; top: 272px;
    text-align: center;
    font-size: 25px; font-weight: 700; letter-spacing: 1.2px;
  }

  /* Back */
  .card-back { top: 619px; background: var(--white); border: 1px solid var(--edge); color: var(--ink); }
  .brand-block { position: absolute; left: 73px; top: 138px; width: 180px; text-align: center; }
  .brand-square { width: 180px; height: 180px; background: var(--orange); }
  .brand-label {
    margin-top: 2px; color: var(--orange);
    font-size: 25px; font-weight: 500; letter-spacing: -0.8px;
  }
  .divider { position: absolute; left: 295px; top: 93px; width: 2px; height: 292px; background: var(--rule); }
  .contact { position: absolute; left: 336px; top: 140px; }
  .person-names { font-size: 31px; font-weight: 700; letter-spacing: 0.2px; line-height: 1.2; }
  .person-role { font-size: 21px; font-weight: 400; margin-top: 3px; }
  .contact-list { list-style: none; margin-top: 32px; }
  .contact-list li {
    display: flex; align-items: center; height: 36px;
    font-size: 25px; font-weight: 400; letter-spacing: 0.2px;
    margin-bottom: 3px;
  }
  .contact-list svg { width: 26px; height: 24px; margin-right: 17px; flex: none; }
</style>
</head>
<body>
<div class="canvas">

  <section class="card card-front">
    <div class="brand-name">Lodgewell<span class="tm">TM</span></div>
    <div class="tagline" style="top:372px">Holiday Let Management &amp; Consulting Specialists</div>
  </section>

  <section class="card card-back">
    <div class="brand-block">
      <div class="brand-square"></div>
      <div class="brand-label">Lodgewell</div>
    </div>
    <div class="divider"></div>
    <div class="contact">
      <div class="person-names">Marta Van Kerr Owen Brisk</div>
      <div class="person-role">Principal Director</div>
      <ul class="contact-list">
        <li>
          <svg viewBox="0 0 26 24" aria-hidden="true">
            <rect x="7" y="1" width="12" height="22" rx="3" fill="none" stroke="var(--orange)" stroke-width="2.2"/>
            <rect x="9.5" y="4" width="7" height="12" fill="var(--orange)"/>
            <circle cx="13" cy="19.5" r="1.4" fill="var(--orange)"/>
          </svg>
          0492637058 0487350216
        </li>
        <li>
          <svg viewBox="0 0 26 24" aria-hidden="true">
            <rect x="1" y="5" width="24" height="15" fill="var(--orange)"/>
            <path d="M1 5 L13 14 L25 5 M1 20 L10 12 M25 20 L16 12" fill="none" stroke="var(--white)" stroke-width="1.6"/>
          </svg>
          enquiries@lodgewell.com.au
        </li>
        <li>
          <svg viewBox="0 0 26 24" aria-hidden="true">
            <g fill="none" stroke="var(--orange)" stroke-width="2">
              <circle cx="13" cy="12" r="10"/>
              <ellipse cx="13" cy="12" rx="4.5" ry="10"/>
              <path d="M3 12 H23 M5 6.5 H21 M5 17.5 H21"/>
            </g>
          </svg>
          www.lodgewell.com.au
        </li>
      </ul>
    </div>
  </section>

</div>
</body>
</html>
```